Business Card Design

My business is writing crime novels to entertain readers. I write legal thrillers and mysteries. I need a card for publishers, agents, other authors, and media.

Industry/Entity Type

Legal

Contact Information for Business Card

Paul Ostrander
www.ostranderthrillers.example
paulbostrander@mailbox.example
0064 27 5139427

```html
<!DOCTYPE html>
<html lang="en">
<head>
<meta charset="utf-8">
<title>Paul Ostrander – Business Card</title>
<link rel="stylesheet" href="https://fonts.googleapis.com/css2?family=Sorts+Mill+Goudy&display=swap">
<style>
  :root {
    --card-grey: #878787;
    --name-rust: #7b3421;
    --ink: #161616;
    --portrait-dark: #2a2b2a;
    --portrait-mid: #4d4d4c;
    --portrait-skin: #b98a78;
  }
  html, body {
    margin: 0;
    padding: 0;
    overflow: hidden;
  }
  body {
    width: 1200px;
    height: 741px;
    background: var(--card-grey);
  }
  .card {
    position: relative;
    width: 1200px;
    height: 741px;
    background: var(--card-grey);
    overflow: hidden;
    font-family: "Sorts Mill Goudy", Georgia, serif;
  }
  .author-name {
    position: absolute;
    left: 42px;
    top: 262px;
    margin: 0;
    font-weight: 400;
    font-size: 100px;
    line-height: 1;
    letter-spacing: 1px;
    color: var(--name-rust);
    z-index: 2;
  }
  .contact-list {
    position: absolute;
    left: 49px;
    top: 536px;
    margin: 0;
    padding: 0;
    list-style: none;
    font-size: 34px;
    line-height: 51px;
    color: var(--ink);
    white-space: nowrap;
    z-index: 2;
  }
  .author-portrait {
    position: absolute;
    left: 725px;
    top: 20px;
    width: 475px;
    height: 721px;
    z-index: 1;
  }
</style>
</head>
<body>
  <div class="card">
    <h1 class="author-name">Paul Ostrander</h1>

    <ul class="contact-list">
      <li>web: www.ostranderthrillers.example</li>
      <li>E-mail: paulbostrander@mailbox.example</li>
      <li>Phone: 0064-27-5139427</li>
    </ul>

    <svg class="author-portrait" viewBox="0 0 510 721" preserveAspectRatio="none" role="img"
         aria-label="Posterised portrait of the author in glasses, white shirt and dark leather jacket">
      <defs>
        <linearGradient id="portrait-tones" x1="0" y1="0" x2="0" y2="1">
          <stop offset="0" stop-color="var(--portrait-skin)"/>
          <stop offset="0.42" stop-color="var(--portrait-skin)"/>
          <stop offset="0.55" stop-color="var(--portrait-mid)"/>
          <stop offset="1" stop-color="var(--portrait-dark)"/>
        </linearGradient>
      </defs>
      <path fill="url(#portrait-tones)"
            d="M170 120 C170 40 230 0 300 5 C370 10 395 70 390 140
               C388 200 370 250 340 280 L380 300 C440 320 490 340 510 370
               L510 721 L0 721 C5 560 20 440 60 400 C100 370 150 350 180 330
               L190 300 C175 260 168 190 170 120 Z"/>
    </svg>
  </div>
</body>
</html>
```